Summit Builders Web Site / Business Cards

Construction Company that specializes in Water and Fire Damage, Residential ReModels, Landscaping and Building ADU (Accessory Dwelling Unit)

Growing and changing families often need additional space, and a remodeling project can often provide that. Adding a new area, or repurposing an existing one can satisfy this requirement.

Other times, homeowners want to update the look in their kitchen or bathroom with more than just a change of cabinetry or vanity doors and drawers. Whatever your needs are, Summit Builders has skilled workers who are bonded and insured, and ready to make your dreams and visions a reality.

Target Market(s)

Home Owners

Industry/Entity Type

Construction Company

Contact Information for Business Card

Center Logo with our information on the corners

Back side to be Logo Only
Contact Info
CSLB License # 4829516
info@summitbuildersca.example
www.summitbuildersca.example

Coding

Coded - Design and coding required

Number of Pages Required

5+ page

Font styles to use
Serif
Sans Serif

Requirements
Must have
• Using our Logo Colors
Home
About Us
Services
Projects / Portfolio
Contact Us
Nice to have
• Colors matching our Logo
Should not have
• Black because it doesnt match our logo

```html
<!DOCTYPE html>
<html lang="en">
<head>
<meta charset="utf-8">
<title>Summit Builders</title>
<link href="https://fonts.googleapis.com/css2?family=Arimo:ital,wght@0,400;0,700;1,400&family=Montserrat:wght@400;500;600&display=swap" rel="stylesheet">
<style>
:root{
  --orange:#f26b1d;
  --orange-deep:#e8560f;
  --rust:#a8410d;
  --rust-dark:#8e370b;
  --ink:#3a2a22;
  --text:#555;
  --muted:#888;
  --line:#e2e2e2;
  --panel:#f3f3f3;
  --white:#fff;
}
*{margin:0;padding:0;box-sizing:border-box}
html,body{width:1200px;height:4140px;overflow:hidden;background:var(--white)}
body{position:relative;font-family:Arimo,Arial,sans-serif;color:var(--ink)}
.abs{position:absolute}
.center{text-align:center}

/* header */
.topbar{left:0;top:0;width:1200px;height:70px}
.brand{left:111px;top:30px;display:flex;align-items:center;gap:12px}
.brand-mark{width:22px;height:22px;background:var(--orange)}
.brand-name{font-family:Montserrat,sans-serif;font-weight:600;font-size:26px;color:var(--ink);letter-spacing:2px;line-height:1}
.license{left:560px;top:24px;font-size:13px;color:var(--white)}
.license b{font-weight:700}
.call{left:775px;top:9px;display:flex;align-items:center;gap:12px;color:var(--white);font-size:13px}
.call-icon{width:40px;height:40px;border-radius:50%;background:var(--white);display:flex;align-items:center;justify-content:center}
.call strong{font-size:20px;font-weight:700}
.nav{top:97px;font-size:13px;color:#333}
.nav.active{color:var(--orange)}
.nav-underline{left:353px;top:131px;width:50px;height:4px;background:var(--orange)}
.nav.quote{color:var(--orange);font-weight:700;font-style:normal}

/* hero */
.hero-photo{left:0;top:137px;width:1200px;height:640px}
.hero-title{left:0;top:330px;width:1200px;font-size:52px;font-weight:700;color:var(--white);text-shadow:0 2px 6px rgba(0,0,0,.35)}
.hero-sub{left:245px;top:396px;width:710px;font-size:14px;line-height:24px;color:var(--white)}
.btn{background:var(--orange);color:var(--white);font-weight:700;font-size:14px;display:flex;align-items:center;justify-content:center}
.hero-btn{left:520px;top:451px;width:160px;height:54px}
.dots{display:flex;gap:4px}
.dot{width:12px;height:12px;border-radius:50%;border:2px solid var(--white)}
.dot.on{background:var(--orange);border-color:var(--orange)}

/* section headings */
.sec-mark{width:24px;height:22px;background:var(--orange);border-radius:2px}
.sec-rule{height:2px;width:90px;background:var(--ink)}
.sec-title{left:0;width:1200px;font-size:44px;font-weight:700;text-transform:uppercase}
.sec-title span{color:var(--orange)}

/* services */
.service{width:440px;text-align:center}
.service-icon{width:82px;height:82px;margin:0 auto;border-radius:8px;background:linear-gradient(135deg,#fbe1cf,#f7c4a2)}
.service h3{font-size:22px;font-weight:700;color:#3a2a22;margin-top:20px}
.service .bar{width:34px;height:2px;background:#b08a3e;margin:14px auto 16px}
.service p{font-size:14px;line-height:26px;color:var(--muted)}
.vdiv{width:1px;background:var(--line)}

/* projects */
.project{top:1877px;width:288px;height:349px}
.project-tag{left:0;top:269px;width:224px;height:50px;clip-path:polygon(0 0,100% 0,82% 100%,0 100%);background:rgba(58,42,34,.85);color:var(--white);font-weight:700;font-size:15px;padding:16px 0 0 40px}
.project-tag.hot{background:var(--orange)}

/* stats */
.stats{left:0;top:2240px;width:1200px;height:250px;background:linear-gradient(90deg,#f47a2a,#f8935a 50%,#f47a2a)}
.stat{width:200px;text-align:center}
.stat-circle{width:130px;height:130px;margin:0 auto;border-radius:50%;background:var(--white);color:var(--orange);font-weight:700;display:flex;align-items:center;justify-content:center;font-size:48px}
.stat-circle.small{font-size:34px}
.stat-label{margin-top:22px;color:var(--white);font-weight:700;font-size:14px}

/* who we are */
.who-card{left:111px;top:2595px;width:978px;height:551px;background:var(--white);box-shadow:0 2px 14px rgba(0,0,0,.12)}
.who-photo{left:0;top:0;width:326px;height:551px;background:linear-gradient(160deg,#f5f5f5,#d9d9d9 60%,#bfb3a8)}
.who-title{left:369px;top:42px;font-size:44px;font-weight:700}
.who-box{width:278px;height:176px;background:var(--panel);padding:20px 18px 20px 22px}
.who-box h4{font-family:Montserrat,sans-serif;font-weight:400;font-size:15.5px;line-height:24px;color:#3a2a22;text-transform:uppercase;white-space:nowrap}
.who-box p{font-family:Montserrat,sans-serif;font-size:12.5px;line-height:26px;color:#666;margin-top:12px}
.who-box .arrow{margin-top:8px}

/* testimonials */
.avatar{width:176px;height:176px;border-radius:50%;background:linear-gradient(135deg,#d8d2cc,#9c948c)}
.quote{width:270px;font-size:12.5px;line-height:24px;font-style:italic;color:#666}
.reviewer{font-weight:700;font-size:15px;color:#555}
.stars{color:var(--orange);font-size:18px;letter-spacing:2px}
.tdot{width:10px;height:10px;border-radius:50%;background:#ccc}
.tdot.on{background:var(--orange)}

/* footer */
.footer-shape{left:0;top:3600px;width:1200px;height:540px}
.newsletter{left:111px;top:3760px;font-family:Montserrat,sans-serif;font-weight:600;font-size:34px;line-height:42px;color:var(--white);text-transform:uppercase}
.email{left:523px;top:3776px;width:562px;height:46px;background:var(--white);border-radius:4px;font-family:Montserrat,sans-serif;font-size:14px;color:#777;padding:13px 20px}
.email-send{right:6px;top:6px;width:38px;height:34px;background:var(--orange);border-radius:3px;display:flex;align-items:center;justify-content:center}
.fcol h5{font-family:Montserrat,sans-serif;font-weight:500;font-size:20px;color:var(--white);margin-bottom:20px}
.fcol li{list-style:none;font-family:Montserrat,sans-serif;font-size:13.5px;color:#fde6d8;line-height:28px}
.social{display:flex;gap:30px;margin-top:4px}
.social span{width:12px;height:12px;border-radius:50%;background:var(--white)}
.copyright{left:0;top:4082px;width:1200px;font-family:Montserrat,sans-serif;font-size:11.5px;color:#fde6d8}
</style>
</head>
<body>

<!-- header -->
<svg class="abs topbar" viewBox="0 0 1200 70" aria-hidden="true">
  <rect x="0" y="0" width="500" height="4" fill="var(--rust)"/>
  <polygon points="496,0 1200,0 1200,64 530,64" fill="var(--orange)"/>
  <polygon points="530,64 1200,64 1200,70 532,70" fill="var(--rust)"/>
</svg>
<div class="abs brand"><span class="brand-mark"></span><span class="brand-name">SUMMIT BUILDERS</span></div>
<div class="abs license">CSLB License # <b>4829516</b></div>
<div class="abs call">
  <span class="call-icon"><svg width="18" height="18" viewBox="0 0 24 24"><path d="M6.6 10.8c1.4 2.8 3.8 5.1 6.6 6.6l2.2-2.2c.3-.3.7-.4 1-.2 1.1.4 2.3.6 3.6.6.6 0 1 .4 1 1V20c0 .6-.4 1-1 1C10.6 21 3 13.4 3 4c0-.6.4-1 1-1h3.5c.6 0 1 .4 1 1 0 1.3.2 2.5.6 3.6.1.3 0 .7-.2 1z" fill="var(--orange)"/></svg></span>
  <span>Call us Today : <strong>661-555-0187</strong></span>
</div>
<nav>
  <div class="abs nav active" style="left:358px">Home</div>
  <div class="abs nav" style="left:456px">About us</div>
  <div class="abs nav" style="left:571px">Services</div>
  <div class="abs nav" style="left:685px">Projects/ Portfolio</div>
  <div class="abs nav" style="left:853px">Contact us</div>
  <div class="abs nav quote" style="left:994px">GET A QUOTE</div>
</nav>
<div class="abs nav-underline"></div>

<!-- hero -->
<svg class="abs hero-photo" viewBox="0 0 1200 640" role="img" aria-label="Photo of a brick family home with a stone mailbox at dusk">
  <defs>
    <linearGradient id="sky" x1="0" y1="0" x2="0" y2="1">
      <stop offset="0" stop-color="#8c8fa8"/>
      <stop offset=".35" stop-color="#c79a9c"/>
      <stop offset=".55" stop-color="#5c5a5e"/>
      <stop offset=".8" stop-color="#2f4428"/>
      <stop offset="1" stop-color="#3a4a52"/>
    </linearGradient>
  </defs>
  <polygon points="0,0 1200,0 1200,534 600,610 0,534" fill="url(#sky)"/>
  <polygon points="0,534 600,610 1200,534 1200,550 600,636 0,550" fill="var(--orange)"/>
  <polygon points="0,550 600,636 1200,550 1200,560 600,640 0,560" fill="#fff"/>
</svg>
<h1 class="abs hero-title center">THE BEST CHOOSE US</h1>
<p class="abs hero-sub center">Lorem ipsum dolor sit amet, consectetur adipiscing elit, sed do eiusmod tempor incididunt ut labore et dolore magna aliqua. Ut enim ad</p>
<div class="abs btn hero-btn">GET STARTED</div>
<div class="abs dots" style="left:570px;top:658px"><span class="dot"></span><span class="dot on"></span><span class="dot"></span><span class="dot"></span></div>

<!-- what we do -->
<div class="abs sec-mark" style="left:588px;top:832px"></div>
<div class="abs sec-rule" style="left:555px;top:856px"></div>
<h2 class="abs sec-title center" style="top:866px">What we do</h2>

<div class="abs service" style="left:133px;top:955px">
  <div class="service-icon" role="img" aria-label="Icon of a house with water and flame"></div>
  <h3>Water &amp; Fire Damage</h3><div class="bar"></div>
  <p>When water or fire strikes, our bonded and insured crews act fast to dry out, clean up and rebuild, restoring walls, floors and roofing so your home is safe, sound and ready to live in again.</p>
</div>
<div class="abs vdiv" style="left:597px;top:963px;height:240px"></div>
<div class="abs service" style="left:623px;top:955px">
  <div class="service-icon" role="img" aria-label="Icon of a builder in front of a house"></div>
  <h3>Residential Remodels</h3><div class="bar"></div>
  <p>From kitchens and bathrooms to whole-home updates, we go beyond new cabinet doors and vanities, reshaping existing rooms so your space fits the way your growing family lives today.</p>
</div>
<div class="abs" style="left:111px;top:1262px;width:978px;height:1px;background:var(--line)"></div>
<div class="abs service" style="left:133px;top:1323px">
  <div class="service-icon" role="img" aria-label="Icon of a garden with trees"></div>
  <h3>Landscaping</h3><div class="bar"></div>
  <p>We design and build outdoor spaces that work as hard as your home does, with patios, walkways, planting, irrigation and hardscape that add comfort, curb appeal and lasting value to your property.</p>
</div>
<div class="abs vdiv" style="left:597px;top:1331px;height:240px"></div>
<div class="abs service" style="left:623px;top:1323px">
  <div class="service-icon" role="img" aria-label="Icon of a small backyard home"></div>
  <h3>ADU Building</h3><div class="bar"></div>
  <p>Need more room? We plan, permit and build accessory dwelling units, turning a backyard or garage into a comfortable space for family, guests or rental income, handled from design to keys.</p>
</div>
<div class="abs btn" style="left:490px;top:1617px;width:220px;height:56px;font-size:13px">VIEW MORE SERVICES</div>

<!-- recent projects -->
<div class="abs sec-mark" style="left:588px;top:1758px"></div>
<div class="abs sec-rule" style="left:555px;top:1782px"></div>
<h2 class="abs sec-title center" style="top:1797px">Recent <span>Projects</span></h2>

<div class="abs project" style="left:0;background:linear-gradient(160deg,#d9d6cf,#9a9890 60%,#4d5560)" role="img" aria-label="Photo of a school building facade">
  <div class="abs project-tag">LOREM IPSUM</div></div>
<div class="abs project" style="left:304px;background:linear-gradient(180deg,#6d7a9a,#8c8c94 50%,#45454a)" role="img" aria-label="Photo of a two-storey suburban house">
  <div class="abs project-tag hot">LOREM IPSUM</div></div>
<div class="abs project" style="left:608px;background:linear-gradient(180deg,#4a6fb8,#5d6f8c 55%,#3d4048)" role="img" aria-label="Photo of a grey family house at evening">
  <div class="abs project-tag">LOREM IPSUM</div></div>
<div class="abs project" style="left:912px;background:linear-gradient(180deg,#dfe6e8,#b4a86a 45%,#4f7a3a 75%,#3a6a80)" role="img" aria-label="Photo of a yellow villa with gardens by the water">
  <div class="abs project-tag">LOREM IPSUM</div></div>

<!-- stats -->
<div class="abs stats" role="img" aria-label="Orange tinted photo of a construction interior"></div>
<div class="abs stat" style="left:134px;top:2278px"><div class="stat-circle">53</div><div class="stat-label">TOTAL PROJECTS</div></div>
<div class="abs stat" style="left:378px;top:2278px"><div class="stat-circle">371</div><div class="stat-label">STAFF MEMBERS</div></div>
<div class="abs stat" style="left:622px;top:2278px"><div class="stat-circle">15</div><div class="stat-label">WORKING IN STATES</div></div>
<div class="abs stat" style="left:866px;top:2278px"><div class="stat-circle small">2,600</div><div class="stat-label">HOURS FOR WORK</div></div>

<!-- who we are -->
<section class="abs who-card">
  <div class="abs who-photo" role="img" aria-label="Photo of a small model house held in an open hand"></div>
  <h2 class="abs who-title">WHO WE ARE</h2>
  <div class="abs who-box" style="left:363px;top:121px">
    <h4>We've repution for<br>excellence</h4>
    <p>Lorem ipsum dolor sit amet, tetur adipiscing elit, sed do eiusmod</p>
    <svg class="arrow" width="24" height="8" viewBox="0 0 24 8"><path d="M0 4h21M18 1l3 3-3 3" stroke="var(--orange)" stroke-width="1.5" fill="none"/></svg>
  </div>
  <div class="abs who-box" style="left:658px;top:121px">
    <h4>We build partnerships</h4>
    <p>Lorem ipsum dolor sit amet,tetur adipiscing elit, sed do eiusmod tempor incididunt ut labore</p>
    <svg class="arrow" width="24" height="8" viewBox="0 0 24 8"><path d="M0 4h21M18 1l3 3-3 3" stroke="var(--orange)" stroke-width="1.5" fill="none"/></svg>
  </div>
  <div class="abs who-box" style="left:363px;top:318px">
    <h4>Guided by commitment</h4>
    <p>Lorem ipsum dolor sit amet, g elit, sed do eiusmod tempor incididunt ut labore et dolore magna aliqua.</p>
    <svg class="arrow" width="24" height="8" viewBox="0 0 24 8"><path d="M0 4h21M18 1l3 3-3 3" stroke="var(--orange)" stroke-width="1.5" fill="none"/></svg>
  </div>
  <div class="abs who-box" style="left:658px;top:318px">
    <h4>A team of professionals</h4>
    <p>Lorem ipsum dolor sit amet, sed do eiusmod tempor incididunt ut labore et dolore magna aliqua.</p>
    <svg class="arrow" width="24" height="8" viewBox="0 0 24 8"><path d="M0 4h21M18 1l3 3-3 3" stroke="var(--orange)" stroke-width="1.5" fill="none"/></svg>
  </div>
</section>

<!-- testimonials -->
<div class="abs sec-mark" style="left:588px;top:3232px"></div>
<div class="abs sec-rule" style="left:555px;top:3256px"></div>
<h2 class="abs sec-title center" style="top:3268px;font-size:34px">What our clients says</h2>

<div class="abs avatar" style="left:110px;top:3336px" role="img" aria-label="Portrait of a client"></div>
<p class="abs quote" style="left:307px;top:3332px">"...and for all the wonderful work you and your crew are doing. Our team has nothing but good things to say - we are really fortunate to have found you for this project!"</p>
<div class="abs reviewer" style="left:307px;top:3474px">Ray Calloway</div>
<div class="abs stars" style="left:462px;top:3470px">★★★★★</div>

<p class="abs quote" style="left:630px;top:3332px;width:285px">"Summit Builders is one of the best general contractors we've worked with. The entire team tactfully delivered a project of exceptional quality while staying on schedule and under budget. We hope to work with"</p>
<div class="abs reviewer" style="left:630px;top:3474px">Dana Whitlock</div>
<div class="abs stars" style="left:785px;top:3470px">★★★★★</div>
<div class="abs avatar" style="left:920px;top:3336px" role="img" aria-label="Portrait of a client"></div>

<div class="abs dots" style="left:578px;top:3545px;gap:4px"><span class="tdot"></span><span class="tdot on"></span><span class="tdot"></span></div>

<!-- footer -->
<svg class="abs footer-shape" viewBox="0 0 1200 540" aria-hidden="true">
  <polygon points="0,100 600,24 1200,100 1200,540 0,540" fill="var(--orange)"/>
  <polygon points="0,120 600,36 1200,120 1200,540 0,540" fill="var(--rust)"/>
  <rect x="0" y="500" width="1200" height="40" fill="var(--rust-dark)"/>
</svg>
<h2 class="abs newsletter">Subscribe<br>our newsletter</h2>
<div class="abs email">Enter your email address
  <div class="abs email-send"><svg width="18" height="18" viewBox="0 0 24 24"><path d="M2 12L22 3l-5 18-6-6-4 5v-7z" fill="none" stroke="#fff" stroke-width="1.8" stroke-linejoin="round"/></svg></div>
</div>

<div class="abs fcol" style="left:111px;top:3888px">
  <h5 style="text-transform:uppercase">Working Hours</h5>
  <ul><li>monday – friday:10:00 – 16:00</li><li>saturday:12:00 – 15:00</li><li>sunday and holidays:09:00 – 12:00</li></ul>
</div>
<div class="abs fcol" style="left:498px;top:3888px">
  <h5>Links</h5>
  <ul><li>Home</li><li>Project</li><li>Blog</li><li>Contact</li></ul>
</div>
<div class="abs fcol" style="left:695px;top:3888px">
  <h5>Legal</h5>
  <ul><li>Faq</li><li>Privacy Policy</li><li>Terms &amp; Conditions</li></ul>
</div>
<div class="abs fcol" style="left:943px;top:3888px">
  <h5>Follow Us</h5>
  <div class="social"><span></span><span></span><span></span><span></span></div>
</div>
<p class="abs copyright center">© Copyrights 2020.The Company Name.All Rights Reserved</p>

</body>
</html>
```